Business card for law firm

Need business card for new law firm. Think confident, authoritative, conservative, but not stuffy or old-fashioned.

Contact Information for Business Card

Content for card - logo (uploaded), plus the following:

Paul Wexbury (larger font)
Managing Partner (larger font, but not as large as name)
Level 9, 41 Tansy Lane
Sydney NSW 2000
Main Tel 02 7346 2190
Direct Tel 02 6273 4415
Email paul@qvlegal.com.au
www.qvlegal.com.au

Letterhead design should include logo plus:
Level 9, 41 Tansy Lane
Sydney NSW 2000
Tel 02 6273 4415
www.qvlegal.com.au

```html
<!DOCTYPE html>
<html lang="en">
<head>
<meta charset="utf-8">
<title>Quayvale Lawyers – Business Card</title>
<link rel="stylesheet" href="https://fonts.googleapis.com/css2?family=Cinzel:wght@400;600&family=Arimo:wght@400;700&display=swap">
<style>
  :root {
    --stage: #2e2e30;
    --card-top: #ffffff;
    --card-bottom: #e9eaec;
    --navy: #14245c;
    --ink: #2a2a2a;
    --muted: #555a66;
    --rule: #9aa0b4;
  }
  * { box-sizing: border-box; margin: 0; padding: 0; }
  html, body { width: 1200px; height: 997px; overflow: hidden; }
  body {
    background: var(--stage);
    position: relative;
    font-family: "Arimo", Arial, sans-serif;
  }
  .card {
    position: absolute;
    width: 540px;
    height: 310px;
    border-radius: 30px;
    background: linear-gradient(160deg, var(--card-top) 0%, var(--card-bottom) 100%);
    overflow: hidden;
    box-shadow: 0 14px 30px rgba(0,0,0,.45);
  }
  .card--front { left: 60px; top: 150px; }
  .card--back  { left: 600px; top: 520px; }

  .band {
    position: absolute;
    left: 0; right: 0;
    top: 222px;
    height: 48px;
  }
  .band__rule {
    position: absolute; left: 0; right: 0;
    height: 3px; background: var(--navy);
  }
  .band__rule--top { top: 0; }
  .band__rule--bottom { bottom: 0; }
  .band__bar {
    position: absolute; left: 0; right: 0;
    top: 9px; height: 30px;
    background: var(--navy);
    display: flex; align-items: center; justify-content: center;
  }
  .band__url {
    color: #fff;
    font-weight: 700;
    font-size: 13px;
    letter-spacing: 5px;
  }

  /* front */
  .brand {
    position: absolute;
    left: 0; right: 0; top: 58px;
    display: flex; flex-direction: column; align-items: center;
    color: var(--navy);
    font-family: "Cinzel", "Times New Roman", serif;
    font-weight: 400;
  }
  .brand__square {
    width: 26px; height: 26px; background: var(--navy); margin-bottom: 20px;
  }
  .brand__name { font-size: 46px; letter-spacing: 2px; line-height: 1; }
  .brand__sub { font-size: 17px; letter-spacing: 16px; margin-top: 10px; padding-left: 16px; }

  /* back */
  .back-brand {
    position: absolute;
    left: 36px; top: 96px; width: 200px;
    display: flex; flex-direction: column; align-items: center;
    color: var(--navy);
    font-family: "Cinzel", "Times New Roman", serif;
    font-weight: 400;
  }
  .back-brand__square { width: 22px; height: 22px; background: var(--navy); margin-bottom: 14px; }
  .back-brand__name { font-size: 28px; letter-spacing: 1px; line-height: 1; }
  .back-brand__sub { font-size: 12px; letter-spacing: 9px; margin-top: 8px; padding-left: 9px; }

  .divider {
    position: absolute;
    left: 262px; top: 40px;
    width: 2px; height: 150px;
    background: linear-gradient(to bottom, transparent, var(--rule), transparent);
  }
  .contact {
    position: absolute;
    left: 292px; top: 38px;
    color: var(--navy);
  }
  .contact__name { font-size: 15px; font-weight: 700; text-transform: uppercase; }
  .contact__role { font-size: 12px; color: var(--ink); margin-bottom: 8px; }
  .contact__address { font-size: 11px; line-height: 1.3; margin-bottom: 8px; }
  .contact__list { list-style: none; font-size: 11.5px; color: var(--ink); }
  .contact__item { display: flex; align-items: center; gap: 7px; margin-bottom: 5px; }
  .contact__icon { width: 14px; height: 14px; flex: none; }
</style>
</head>
<body>

  <section class="card card--front" aria-label="Card front">
    <div class="brand">
      <div class="brand__square"></div>
      <div class="brand__name">QUAYVALE</div>
      <div class="brand__sub">LAWYERS</div>
    </div>
    <div class="band">
      <div class="band__rule band__rule--top"></div>
      <div class="band__bar"><span class="band__url">www.qvlegal.com</span></div>
      <div class="band__rule band__rule--bottom"></div>
    </div>
  </section>

  <section class="card card--back" aria-label="Card back">
    <div class="back-brand">
      <div class="back-brand__square"></div>
      <div class="back-brand__name">QUAYVALE</div>
      <div class="back-brand__sub">LAWYERS</div>
    </div>
    <div class="divider"></div>
    <div class="contact">
      <p class="contact__name">Paul Wexbury</p>
      <p class="contact__role">Managing Partner</p>
      <p class="contact__address">Level 9, 41 Tansy Lane<br>Sydney NSW 2000</p>
      <ul class="contact__list">
        <li class="contact__item">
          <svg class="contact__icon" viewBox="0 0 14 14" aria-hidden="true"><circle cx="7" cy="7" r="7" fill="#14245c"/><path d="M4 5.2c0-.8.6-1.2 3-1.2s3 .4 3 1.2v.6H8.6v-.7H5.4v.7H4zM4.6 6.5h4.8l.6 3.3H4z" fill="#fff"/></svg>
          02 7346 2190
        </li>
        <li class="contact__item">
          <svg class="contact__icon" viewBox="0 0 14 14" aria-hidden="true"><circle cx="7" cy="7" r="7" fill="#14245c"/><rect x="5" y="3" width="4" height="8" rx=".8" fill="#fff"/><rect x="5.6" y="4" width="2.8" height="4.6" fill="#14245c"/></svg>
          02 6273 4415
        </li>
        <li class="contact__item">
          <svg class="contact__icon" viewBox="0 0 14 14" aria-hidden="true"><circle cx="7" cy="7" r="7" fill="#14245c"/><rect x="3.5" y="4.5" width="7" height="5" fill="#fff"/><path d="M3.5 4.5 7 7.4l3.5-2.9" fill="none" stroke="#14245c" stroke-width=".8"/></svg>
          paul@qvlegal.com.au
        </li>
      </ul>
    </div>
    <div class="band">
      <div class="band__rule band__rule--top"></div>
      <div class="band__bar"><span class="band__url">www.qvlegal.com</span></div>
      <div class="band__rule band__rule--bottom"></div>
    </div>
  </section>

</body>
</html>
```